Velantra Slim Label Design

Hi,
Our company is Harbor Crest Labs.
We sell health and beauty product online directly to consumers. Our primary target audience is women.
I would like a product label for a new supplement we are launching called "Velantra Slim." It is a weight loss supplement recommended by Dr. Pell. He says it will "burn your belly fat from the inside out."
The Product Label should say "Velantra Slim" along with our company name "Harbor Crest Labs"
The design is up to you to come up with, but should be simple and elegant. The bottle is white and the label needs to be 2" by 5.5"
I would like both the label deign in a format ready to print as well as a 3D Rendering of the label design on the bottle, in a minimum resolution of 1200 x 1200 on a pure white background for display on our website.
I am attaching sample images of a label with suggested use, caution, supplement facts, etc. - these need to be included on the label
I am also attaching some product shots of product that is similar to ours for possible inspiration.
Instead of Quobelline Laboratories, I need it to read
Harbor Crest Labs
1-855-310-4827
www.HarborCrestLabs.example
We will also need our UPC code on the label. You can use any UPC example you wish for now, but before the final design we will assign you our actual UPC code for final delivery.
If you have any questions, please feel free to ask.
Target Market(s)
Primarily for women. Maybe middle aged women who are looking to drop some weight.
Industry/Entity Type
Health
Look and feel

```html
<!DOCTYPE html>
<html lang="en">
<head>
<meta charset="utf-8">
<title>Velantra Slim Label Variants</title>
<link rel="stylesheet" href="https://fonts.googleapis.com/css2?family=Arimo:wght@400;700&family=PT+Sans+Narrow:wght@400;700&display=swap">
<style>
  :root {
    --page-bg: #ededee;
    --label-white: #ffffff;
    --lime: #a9cf3a;
    --lime-soft: #e4f0b8;
    --tab-red: #d9151c;
    --title-blue: #1f5fa6;
    --title-blue-dark: #123f78;
    --body-grey: #4a4f55;
    --leaf-green: #5f9a2c;
    --leaf-light: #9bcb5a;

    --blue-light: #8ec3f0;
    --blue-mid: #2d79c6;
    --blue-dark: #153e8c;

    --purple-light: #c79be6;
    --purple-mid: #8b3fc2;
    --purple-dark: #541c86;

    --green-light: #a7e27a;
    --green-mid: #3fae2c;
    --green-dark: #1c6f1f;
  }

  * { box-sizing: border-box; margin: 0; padding: 0; }

  html, body {
    width: 1200px;
    height: 900px;
    overflow: hidden;
    background: var(--page-bg);
  }

  .label-row {
    position: relative;
    width: 1200px;
    height: 900px;
    display: flex;
    justify-content: center;
    align-items: center;
    gap: 45px;
  }

  .label {
    position: relative;
    width: 340px;
    height: 440px;
    background: var(--label-white);
    overflow: hidden;
    box-shadow: 0 2px 10px rgba(0,0,0,0.08);
  }

  .label--blue   { --wave-light: var(--blue-light);   --wave-mid: var(--blue-mid);   --wave-dark: var(--blue-dark); }
  .label--purple { --wave-light: var(--purple-light); --wave-mid: var(--purple-mid); --wave-dark: var(--purple-dark); }
  .label--green  { --wave-light: var(--green-light);  --wave-mid: var(--green-mid);  --wave-dark: var(--green-dark); }

  .label__sky {
    position: absolute;
    inset: 0 0 auto 0;
    height: 150px;
    background: linear-gradient(to bottom, var(--lime) 0%, var(--lime-soft) 55%, var(--label-white) 100%);
  }

  .label__brand-tab {
    position: absolute;
    top: 0;
    left: 50%;
    transform: translateX(-50%);
    width: 200px;
    height: 44px;
    background: var(--tab-red);
    border-radius: 0 0 10px 10px;
    display: flex;
    align-items: center;
    justify-content: center;
    color: var(--label-white);
    font-family: "PT Sans Narrow", sans-serif;
    font-size: 22px;
    font-weight: 400;
  }

  .label__title {
    position: absolute;
    top: 78px;
    left: 0;
    right: 0;
    text-align: center;
    font-family: "Arimo", sans-serif;
    font-weight: 700;
    color: var(--title-blue);
    line-height: 1;
    text-shadow: 0 2px 0 var(--label-white), 0 3px 3px rgba(18,63,120,0.25);
  }

  .label__title-main { display: block; font-size: 50px; letter-spacing: 0.5px; }
  .label__title-sub  { display: block; font-size: 38px; margin-top: 6px; color: var(--title-blue-dark); }

  .label__ingredient {
    position: absolute;
    top: 196px;
    left: 18px;
    padding-right: 10px;
    border-right: 2px solid var(--title-blue);
    font-family: "Arimo", sans-serif;
    font-size: 12.5px;
    line-height: 1.35;
    color: var(--body-grey);
  }

  .label__leaf {
    position: absolute;
    top: 180px;
    right: 18px;
    width: 110px;
    height: 100px;
    border-radius: 50% 40% 50% 45%;
    background: radial-gradient(circle at 40% 40%, var(--leaf-light), var(--leaf-green));
    z-index: 2;
  }

  .label__wave {
    position: absolute;
    left: 0;
    bottom: 0;
    width: 340px;
    height: 190px;
  }

  .label__footer {
    position: absolute;
    left: 18px;
    right: 18px;
    bottom: 26px;
    display: flex;
    justify-content: space-between;
    align-items: flex-end;
    color: var(--label-white);
    font-family: "Arimo", sans-serif;
    z-index: 3;
  }

  .label__type { font-size: 14px; letter-spacing: 0.3px; }

  .label__count { text-align: center; line-height: 1; }
  .label__count-num { display: block; font-size: 20px; }
  .label__count-unit { display: block; font-size: 8px; letter-spacing: 0.5px; margin-top: 2px; }
</style>
</head>
<body>
<main class="label-row">

  <section class="label label--blue">
    <div class="label__sky"></div>
    <div class="label__brand-tab">Harbor Crest Labs</div>
    <h1 class="label__title">
      <span class="label__title-main">VELANTRA</span>
      <span class="label__title-sub">SLIM</span>
    </h1>
    <p class="label__ingredient">COLEUS FORSKOHLII<br>ROOT EXTRACT</p>
    <div class="label__leaf" role="img" aria-label="Sprig of fresh green coleus leaves"></div>
    <svg class="label__wave" viewBox="0 0 340 190" aria-hidden="true">
      <path d="M0 70 C110 30 230 20 340 45 V190 H0 Z" fill="var(--wave-light)"/>
      <path d="M0 95 C120 60 230 50 340 75 V190 H0 Z" fill="var(--wave-mid)"/>
      <path d="M0 120 C130 90 240 80 340 100 V190 H0 Z" fill="var(--wave-dark)"/>
      <path d="M0 88 C120 52 230 42 340 66" fill="none" stroke="#ffffff" stroke-width="2" opacity="0.8"/>
    </svg>
    <div class="label__footer">
      <span class="label__type">DIETARY SUPPLEMENT</span>
      <span class="label__count"><span class="label__count-num">30</span><span class="label__count-unit">CAPSULES</span></span>
    </div>
  </section>

  <section class="label label--purple">
    <div class="label__sky"></div>
    <div class="label__brand-tab">Harbor Crest Labs</div>
    <h2 class="label__title">
      <span class="label__title-main">VELANTRA</span>
      <span class="label__title-sub">SLIM</span>
    </h2>
    <p class="label__ingredient">COLEUS FORSKOHLII<br>ROOT EXTRACT</p>
    <div class="label__leaf" role="img" aria-label="Sprig of fresh green coleus leaves"></div>
    <svg class="label__wave" viewBox="0 0 340 190" aria-hidden="true">
      <path d="M0 70 C110 30 230 20 340 45 V190 H0 Z" fill="var(--wave-light)"/>
      <path d="M0 95 C120 60 230 50 340 75 V190 H0 Z" fill="var(--wave-mid)"/>
      <path d="M0 120 C130 90 240 80 340 100 V190 H0 Z" fill="var(--wave-dark)"/>
      <path d="M0 88 C120 52 230 42 340 66" fill="none" stroke="#ffffff" stroke-width="2" opacity="0.8"/>
    </svg>
    <div class="label__footer">
      <span class="label__type">DIETARY SUPPLEMENT</span>
      <span class="label__count"><span class="label__count-num">30</span><span class="label__count-unit">CAPSULES</span></span>
    </div>
  </section>

  <section class="label label--green">
    <div class="label__sky"></div>
    <div class="label__brand-tab">Harbor Crest Labs</div>
    <h2 class="label__title">
      <span class="label__title-main">VELANTRA</span>
      <span class="label__title-sub">SLIM</span>
    </h2>
    <p class="label__ingredient">COLEUS FORSKOHLII<br>ROOT EXTRACT</p>
    <div class="label__leaf" role="img" aria-label="Sprig of fresh green coleus leaves"></div>
    <svg class="label__wave" viewBox="0 0 340 190" aria-hidden="true">
      <path d="M0 70 C110 30 230 20 340 45 V190 H0 Z" fill="var(--wave-light)"/>
      <path d="M0 95 C120 60 230 50 340 75 V190 H0 Z" fill="var(--wave-mid)"/>
      <path d="M0 120 C130 90 240 80 340 100 V190 H0 Z" fill="var(--wave-dark)"/>
      <path d="M0 88 C120 52 230 42 340 66" fill="none" stroke="#ffffff" stroke-width="2" opacity="0.8"/>
    </svg>
    <div class="label__footer">
      <span class="label__type">DIETARY SUPPLEMENT</span>
      <span class="label__count"><span class="label__count-num">30</span><span class="label__count-unit">CAPSULES</span></span>
    </div>
  </section>

</main>
</body>
</html>
```